Silver cove Convenience store

I have just purchased a business you can see picture its very dated. It needs a fresh feel on top to say silver cove Convenience store.
Underneath it could say something like groceries, fruit vegies and more. On the window it would be beter left clean on the top but at the bottom maybee pictures of fresh fruits vegetables and general items a high end gourmet feel
Updates
The photograph i have sent is the shop i purchased, and the old signage. Its very outdated i need it to be very clear and in date Added Wednesday, October 12, 2016
Im looking for it to have a more gourmet or high end feel Added Friday, October 14, 2016

```html
<!DOCTYPE html>
<html lang="en">
<head>
<meta charset="utf-8">
<title>Silver Cove Convenience Store – Fascia Sign</title>
<link rel="stylesheet" href="https://fonts.googleapis.com/css2?family=Dancing+Script:wght@700&family=Delius&display=swap">
<style>
  :root {
    --backdrop: #eef0ea;
    --sign-green: #a6c40a;
    --sign-green-light: #b4d014;
    --frame-dark: #3d4046;
    --frame-edge: #c9cfc2;
    --script-grey: #6a6a70;
    --hours-white: #ffffff;
  }
  html, body {
    margin: 0;
    padding: 0;
    width: 1200px;
    height: 1030px;
    overflow: hidden;
    background: var(--backdrop);
  }
  .canvas {
    position: relative;
    width: 1200px;
    height: 1030px;
    display: flex;
    align-items: center;
    justify-content: center;
  }
  .fascia-sign {
    box-sizing: border-box;
    width: 1110px;
    height: 160px;
    background: linear-gradient(180deg, var(--sign-green-light) 0%, var(--sign-green) 100%);
    border: 6px solid var(--frame-dark);
    box-shadow: inset 0 0 0 3px var(--frame-edge);
    display: flex;
    align-items: center;
    justify-content: space-between;
    padding: 0 36px 0 48px;
  }
  .fascia-sign__hours {
    font-family: "Delius", sans-serif;
    font-size: 52px;
    color: var(--hours-white);
    letter-spacing: 1px;
  }
  .fascia-sign__name {
    font-family: "Dancing Script", cursive;
    font-weight: 700;
    font-size: 92px;
    color: var(--script-grey);
    line-height: 1;
    padding-top: 6px;
  }
</style>
</head>
<body>
  <main class="canvas">
    <div class="fascia-sign">
      <span class="fascia-sign__hours">24/24</span>
      <span class="fascia-sign__name">Silver Cove</span>
      <span class="fascia-sign__hours">24/24</span>
    </div>
  </main>
</body>
</html>
```